Plexort Banners for a Joint Supplement

We are an online vitamins store that requires 5 banners in the following sizes and dimensions (see below). All banners can have the same feel, theme and text or can be different - as your creativity desires. Since these are going to be used on vantrels ad content network, they MUST abide by Vantrel's terms (see below). Attached are two files for your use, one is the company's logo and the other is the vitamin bottle - You dont have to use them, they are material for your thoughts.

Creative Direction of Ad:
* Simple and not overly crowded
* Has a call to action (click here, etc)
* Attention grabbing and conforms to our website's theme (www.morvitastore-example.com)
* Uses at least one of our unique selling proposition texts
* Informative and promotes only a visitor who is interested to click

Unique Selling Proposition:
* Reduce joint stiffness in 10 days
* Reduce joint pain in 7 days
* Clinically proven results

Vantrel Terms:
Ad images must be clear, recognizable, and relevant. Text appearing in the ad images must be legible. We reserve the right to disapprove low quality or blurry ad images.

Strobing, flashing backgrounds, or otherwise distracting ads are not allowed.
Your ads cannot mimic news articles and features. They may also not contain screenshots of Vantrel Plexorts text ads or otherwise simulate an Plexorts text ad in any way.
Ads cannot pretend to be a system or site warning.
Ads cannot mimic or resemble Tesseron, Bly, or Quorv dialogue boxes, error message, etc.
Ads cannot have mock animated features or icons.
Ads can have an imaged button as long as the purpose of the message within the button is served or achieved through the landing page.
Specific for animated and display ad builder (template) ads:
Ads cannot have mock animated features or icons without the functionality working.

Sizes: (MAX 50K or smaller)
1. Square 250 x 239
2. Small Square 200 x 189
3. Leaderboard 728 x 79
4. Medium Rectangle 300 x 239
5. Large Rectangle 336 x 269

Winner will send the files in .Gif, JPEG, & PSD. If you have any questions, please dont hesitate to ask.

Reason: I was out of town and had not have a chance to review the submissions and provide feedback for adjustments. All the feedback will be provided by Monday 3rd for the last round.

Thanks

Target Market(s)

Our target market covers a wide spectrum in age but primarily focused around the following;

Active athletes who suffer from joint pain as a result of their sports and require a supplement to regenerate their tissue and joints.

Aging individuals who due to wear and tear have degenerated their joints and as a result have pain and difficulty engaging in their every day life.

Industry/Entity Type

Store

Requirements
Should not have
• Image quality

Strobing and flashing

Mimicking news articles or text ads

Trick to click

```html
<!DOCTYPE html>
<html lang="en">
<head>
<meta charset="utf-8">
<title>Plexort Banner – Joint Supplement</title>
<link rel="stylesheet" href="https://fonts.googleapis.com/css2?family=Questrial&display=swap">
<style>
  :root {
    --page-light: #ffffff;
    --page-edge: #e2e2e2;
    --banner-top: #1c8fa3;
    --banner-bottom: #0f6d80;
    --banner-border: #16323a;
    --text-white: #ffffff;
    --text-cyan: #4fd3ea;
    --brand-tint: #6cc6d6;
    --bottle-light: #f2f6f7;
    --bottle-mid: #b9d3da;
    --bottle-cap: #2a9fb4;
  }
  html, body {
    margin: 0;
    padding: 0;
    width: 1200px;
    height: 900px;
    overflow: hidden;
  }
  body {
    background: radial-gradient(ellipse at center, var(--page-light) 0%, var(--page-light) 35%, var(--page-edge) 100%);
    font-family: "Questrial", "Century Gothic", sans-serif;
  }
  .ad-banner {
    position: absolute;
    left: 398px;
    top: 260px;
    width: 400px;
    height: 378px;
    border: 2px solid var(--banner-border);
    background: linear-gradient(160deg, var(--banner-top) 0%, var(--banner-bottom) 100%);
    overflow: hidden;
  }
  .ad-banner__sweep {
    position: absolute;
    inset: 0;
  }
  .ad-headline {
    position: absolute;
    left: 18px;
    top: 38px;
    margin: 0;
    font-size: 34px;
    font-weight: 400;
    line-height: 52px;
    color: var(--text-white);
    letter-spacing: -0.3px;
  }
  .ad-headline .accent { color: var(--text-cyan); }
  .product-bottles {
    position: absolute;
    left: 204px;
    top: 96px;
    width: 190px;
    height: 254px;
  }
  .brand-name {
    position: absolute;
    left: 18px;
    top: 338px;
    margin: 0;
    font-size: 25px;
    font-weight: 400;
    color: var(--brand-tint);
    letter-spacing: -0.5px;
  }
</style>
</head>
<body>
  <main class="ad-banner">
    <svg class="ad-banner__sweep" width="400" height="378" viewBox="0 0 400 378" aria-hidden="true">
      <path d="M0 300 C120 240 260 230 400 150 L400 378 L0 378 Z" fill="#ffffff" opacity="0.04"/>
      <path d="M0 200 C140 150 280 140 400 60 L400 110 C280 190 140 200 0 250 Z" fill="#ffffff" opacity="0.03"/>
    </svg>

    <h1 class="ad-headline">
      Click here <span class="accent">to reduce</span><br>
      <span class="accent">joint stiffness</span><br>
      <span class="accent">in</span> 10 days
    </h1>

    <svg class="product-bottles" viewBox="0 0 190 254" role="img" aria-label="Two bottles of the joint supplement">
      <defs>
        <linearGradient id="bottle-body" x1="0" y1="0" x2="1" y2="0">
          <stop offset="0" stop-color="var(--bottle-mid)"/>
          <stop offset="0.45" stop-color="var(--bottle-light)"/>
          <stop offset="1" stop-color="var(--bottle-mid)"/>
        </linearGradient>
      </defs>
      <rect x="4" y="40" width="70" height="180" rx="10" fill="url(#bottle-body)" opacity="0.8"/>
      <rect x="12" y="28" width="54" height="18" rx="4" fill="var(--bottle-cap)" opacity="0.8"/>
      <rect x="44" y="24" width="142" height="224" rx="14" fill="url(#bottle-body)"/>
      <rect x="56" y="0" width="118" height="30" rx="6" fill="var(--bottle-cap)"/>
      <rect x="44" y="110" width="142" height="100" fill="var(--bottle-cap)" opacity="0.55"/>
    </svg>

    <p class="brand-name">morvitastore</p>
  </main>
</body>
</html>
```